KLD Photography Editing & Support Services for Real Estate

We require a double sided A4 flyer to promote our photography services to real estate agencies.
This particular service is targeted to rural areas where reliable, professional and highly skilled photographers are difficult to source. We teach the agent how to photograph, they upload files to a server and we take care of the rest (image editing, quality control and delivery). This will give the agents flexibility with when to shoot and eliminates the stress of managing a photographer / contractor. We offer a 1 day face to face training session and competitive packages for equipment start up.
We would like the flyer to look clean & very professional. The flyer should showcase samples of our work to highlight what can be achieved by using our services. We like the look of a black or dark background behind the text and feel that would look nice with our photographs provided. Otherwise open to your suggestions and ideas.
TEXT FOR FLYER:
Welcome to the KLD Real Estate Photography Editing and Support Service
• Take your real estate business to the next level by providing impressive real estate imagery that makes you stands out from the competition
• Omit the stress of trying to find a good photographer or managing an unreliable one and hence have more time to focus on other aspects of your business
• Showcase your listings with better quality and more impactful photographs than your competitors thereby increasing potential for a quick sale
• Great first impressions matter and you will achieve this by looking and feeling more professional. This will attract and retain more future clients.
HOW IT WORKS
• We understand that your time is valuable, so let us handle the editing and delivery of your images. You shoot, and we take care of the rest.
• Images are edited and delivered within 1 working day
INCLUSIONS:
• Full day face to face training (we come to you) and instructional handbook
• We will teach you everything you need to know about your equipment and how to take stunning real estate photographs
• Service turnaround within 1 working day
• Free HELP desk service Mon-Fri
• 12 month Exclusivity (rural towns only) for a limited time
INVESTMENT
• 99 per listing for us to manage images including editing, quality control and delivery (10 Images)
• Ask us about competitive packages for photography equipment if required
SUMMARY
The KLD Real Estate Photography Editing and Support Service is the perfect solution for busy real estate professionals who want to take their business to the next level. Our service is affordable, flexible, and designed to help you showcase your listings in the best possible light.
Contact us today to learn more about how we can help you.

```html
<!DOCTYPE html>
<html lang="en">
<head>
<meta charset="utf-8">
<title>KLD Real Estate Photography Editing &amp; Support Service Flyer</title>
<link href="https://fonts.googleapis.com/css2?family=Cinzel:wght@500;600&family=Poppins:wght@300;400;500;600&display=swap" rel="stylesheet">
<style>
  :root {
    --backdrop: #c9c9c9;
    --navy: #0d1839;
    --navy-deep: #091129;
    --panel: #1a2648;
    --gold: #b0834f;
    --gold-light: #d79a55;
    --white: #ffffff;
    --muted: #d9dce4;
  }
  * { margin: 0; padding: 0; box-sizing: border-box; }
  html, body { width: 931px; height: 1200px; overflow: hidden; }
  body {
    background: var(--backdrop);
    font-family: "Poppins", sans-serif;
    color: var(--white);
    position: relative;
  }
  .page {
    position: absolute;
    top: 289px;
    width: 440px;
    height: 622px;
    background: linear-gradient(180deg, var(--navy) 0%, var(--navy-deep) 100%);
    overflow: hidden;
    box-shadow: 2px 3px 6px rgba(0,0,0,0.25);
  }
  .page--front { left: 15px; }
  .page--back { left: 476px; }
  .abs { position: absolute; }

  /* Brand */
  .brand { left: 0; right: 0; top: 36px; text-align: center; }
  .brand__name {
    font-weight: 300; font-size: 15px; letter-spacing: 4px;
    color: var(--muted); text-transform: uppercase;
  }
  .brand__role {
    margin-top: 8px; font-weight: 300; font-size: 7px; letter-spacing: 2.4px;
    color: var(--muted); text-transform: uppercase;
  }

  /* Headline banner */
  .headline {
    left: 37px; top: 113px; width: 367px; height: 98px;
    background: rgba(176,131,79,0.93); text-align: center; z-index: 2;
    padding-top: 14px;
  }
  .headline__kicker {
    font-size: 9.5px; letter-spacing: 2.2px; text-transform: uppercase; color: var(--navy-deep);
    font-weight: 400;
  }
  .headline__title {
    font-family: "Cinzel", serif; font-weight: 600; font-size: 22.5px; line-height: 24px;
    margin-top: 5px; color: var(--white); letter-spacing: 0.4px;
  }

  .photo { display: block; }
  .photo--hero {
    left: 0; top: 192px; width: 440px; height: 218px;
    background: linear-gradient(180deg, #5a4330 0%, #2f4f78 35%, #a77b4f 70%, #6a5442 100%);
  }

  /* Feature boxes */
  .feature {
    top: 431px; width: 85px; height: 98px; background: var(--panel);
    text-align: center; padding: 8px 5px 0;
  }
  .feature svg { width: 20px; height: 20px; }
  .feature__text { font-size: 5.6px; line-height: 6.9px; margin-top: 3px; color: var(--white); }

  /* How it works */
  .how { left: 32px; top: 550px; display: flex; align-items: center; }
  .how__label { font-size: 10px; line-height: 12px; font-weight: 300; text-transform: uppercase; }
  .how__label strong { font-weight: 600; display: block; }
  .how__rule { width: 1px; height: 26px; background: var(--gold); margin: 0 12px 0 13px; }
  .ticks { list-style: none; }
  .ticks li {
    position: relative; padding-left: 8px; font-size: 5.7px; line-height: 6.6px; margin-bottom: 2px;
  }
  .ticks li svg { position: absolute; left: 0; top: 1px; width: 5px; height: 5px; }
  .how .ticks { width: 200px; }

  .contact {
    left: 32px; top: 582px; font-size: 10px; letter-spacing: 1px; font-weight: 300;
    display: flex; align-items: center; white-space: nowrap;
  }
  .contact svg { width: 8px; height: 8px; margin-right: 2px; }
  .contact__sep { margin: 0 14px; color: var(--muted); }
  .contact__web em { font-style: normal; color: var(--gold-light); }

  .avatar { width: 58px; height: 58px; border-radius: 50%;
    background: radial-gradient(circle at 50% 40%, #8a5a45 0%, #3a2320 55%, #1a1212 100%);
    border: 1px solid var(--white);
  }
  .avatar-label {
    background: var(--gold); color: var(--white); font-size: 7px; padding: 1px 5px;
    white-space: nowrap; text-align: center; width: 66px;
  }

  /* Back page */
  .inclusions__label { left: 31px; top: 56px; font-size: 10px; font-weight: 600; letter-spacing: 0.2px; }
  .inclusions__rule { left: 109px; top: 31px; width: 1px; height: 61px; background: var(--gold); }
  .inclusions__list { left: 120px; top: 30px; width: 300px; }
  .inclusions__list li { margin-bottom: 5px; font-size: 5.6px; }

  .investment {
    left: 37px; top: 115px; width: 367px; height: 77px; background: var(--gold); z-index: 2;
    text-align: center; padding-top: 9px;
  }
  .investment__title { font-size: 10px; font-weight: 600; color: var(--navy-deep); letter-spacing: 0.3px; }
  .investment__items { display: flex; justify-content: center; align-items: center; margin-top: 8px; }
  .investment__item { display: flex; align-items: center; text-align: left; font-size: 6.5px; line-height: 7.5px; }
  .investment__item svg { width: 24px; height: 24px; margin-right: 6px; flex: none; }
  .investment__divider { width: 1px; height: 24px; background: var(--navy-deep); opacity: 0.6; margin: 0 22px 0 16px; }

  .summary {
    left: 32px; top: 528px; width: 310px; border-left: 1px solid var(--gold); padding-left: 5px;
    font-size: 5.6px; line-height: 6.6px;
  }
  .cta { left: 32px; top: 564px; font-size: 7.6px; letter-spacing: 0.3px; text-transform: uppercase; }
</style>
</head>
<body>

<!-- FRONT -->
<section class="page page--front" aria-label="Flyer front">
  <div class="abs brand">
    <p class="brand__name">Marcus Hale</p>
    <p class="brand__role">Photographer</p>
  </div>

  <div class="abs headline">
    <p class="headline__kicker">Welcome to the KLD Real Estate</p>
    <h1 class="headline__title">Photography Editing<br>&amp; Support Service</h1>
  </div>

  <div class="abs photo photo--hero" role="img" aria-label="Photograph of a timber-lined living room with tall gabled windows at dusk"></div>

  <div class="abs feature" style="left:32px">
    <svg viewBox="0 0 24 24" fill="none" stroke="#d79a55" stroke-width="1.3"><path d="M3 11l9-7 9 7"/><path d="M5 10v10h14V10"/><rect x="10" y="14" width="4" height="6"/></svg>
    <p class="feature__text">Take your real estate business to the next level by providing impressive real estate imagery that makes you stands out from the competition</p>
  </div>
  <div class="abs feature" style="left:129px">
    <svg viewBox="0 0 24 24" fill="none" stroke="#d79a55" stroke-width="1.3"><rect x="3" y="7" width="18" height="13" rx="2"/><circle cx="12" cy="13.5" r="4"/><path d="M9 7l1.5-3h3L15 7"/></svg>
    <p class="feature__text">Omit the stress of trying to find a good photographer or managing an unreliable one and hence have more time to focus on other aspects of your business</p>
  </div>
  <div class="abs feature" style="left:226px">
    <svg viewBox="0 0 24 24" fill="none" stroke="#d79a55" stroke-width="1.3"><rect x="5" y="4" width="13" height="17" rx="1"/><path d="M8 9h7M8 12h7M8 15h4"/><circle cx="17" cy="18" r="3"/><path d="M15.8 18l.9.9 1.6-1.7"/></svg>
    <p class="feature__text">Showcase your listings with better quality and more impactful photographs than your competitors thereby increasing potential for a quick sale</p>
  </div>
  <div class="abs feature" style="left:323px">
    <svg viewBox="0 0 24 24" fill="none" stroke="#d79a55" stroke-width="1.3"><path d="M3 17l4-3h5l3 2h4"/><path d="M7 20h11l3-3"/><circle cx="13" cy="8" r="3"/><path d="M13 2v1M8 5l1 1M18 5l-1 1"/></svg>
    <p class="feature__text">Great first impressions matter and you will achieve this by looking and feeling more professional. This will attract and retain more future clients.</p>
  </div>

  <div class="abs how">
    <p class="how__label">How it<strong>Works</strong></p>
    <span class="how__rule"></span>
    <ul class="ticks">
      <li><svg viewBox="0 0 10 10" fill="none" stroke="#d79a55" stroke-width="1.2"><rect x="0.6" y="0.6" width="8.8" height="8.8"/><path d="M2.5 5l2 2 3.5-4"/></svg>We understand that your time is valuable, so let us handle the editing and delivery of your images. You shoot, and we take care of the rest.</li>
      <li><svg viewBox="0 0 10 10" fill="none" stroke="#d79a55" stroke-width="1.2"><rect x="0.6" y="0.6" width="8.8" height="8.8"/><path d="M2.5 5l2 2 3.5-4"/></svg>Images are edited and delivered within 1 working day</li>
    </ul>
  </div>

  <p class="abs contact">
    <svg viewBox="0 0 24 24" fill="#d79a55"><path d="M6.6 10.8a15 15 0 006.6 6.6l2.2-2.2c.3-.3.7-.4 1-.2 1.1.4 2.3.6 3.6.6.6 0 1 .4 1 1V20c0 .6-.4 1-1 1A17 17 0 013 4c0-.6.4-1 1-1h3.5c.6 0 1 .4 1 1 0 1.3.2 2.5.6 3.6.1.3 0 .7-.2 1z"/></svg>
    +61 400 555 017<span class="contact__sep">|</span><span class="contact__web">www.<em>marcushale</em>.com.au</span>
  </p>

  <div class="abs avatar" style="left:346px;top:539px" role="img" aria-label="Portrait of Marcus Hale"></div>
  <p class="abs avatar-label" style="left:342px;top:583px">Marcus Hale</p>
</section>

<!-- BACK -->
<section class="page page--back" aria-label="Flyer back">
  <h2 class="abs inclusions__label">INCLUSIONS</h2>
  <span class="abs inclusions__rule"></span>
  <ul class="abs ticks inclusions__list">
    <li><svg viewBox="0 0 10 10" fill="none" stroke="#d79a55" stroke-width="1.2"><rect x="0.6" y="0.6" width="8.8" height="8.8"/><path d="M2.5 5l2 2 3.5-4"/></svg>Full day face to face training (we come to you) and instructional handbook</li>
    <li><svg viewBox="0 0 10 10" fill="none" stroke="#d79a55" stroke-width="1.2"><rect x="0.6" y="0.6" width="8.8" height="8.8"/><path d="M2.5 5l2 2 3.5-4"/></svg>We will teach you everything you need to know about your equipment and how to take stunning real estate photographs</li>
    <li><svg viewBox="0 0 10 10" fill="none" stroke="#d79a55" stroke-width="1.2"><rect x="0.6" y="0.6" width="8.8" height="8.8"/><path d="M2.5 5l2 2 3.5-4"/></svg>Service turnaround within 1 working day</li>
    <li><svg viewBox="0 0 10 10" fill="none" stroke="#d79a55" stroke-width="1.2"><rect x="0.6" y="0.6" width="8.8" height="8.8"/><path d="M2.5 5l2 2 3.5-4"/></svg>Free HELP desk service Mon-Fri</li>
    <li><svg viewBox="0 0 10 10" fill="none" stroke="#d79a55" stroke-width="1.2"><rect x="0.6" y="0.6" width="8.8" height="8.8"/><path d="M2.5 5l2 2 3.5-4"/></svg>12 month Exclusivity (rural towns only) for a limited time</li>
  </ul>

  <div class="abs investment">
    <h2 class="investment__title">INVESTMENT</h2>
    <div class="investment__items">
      <div class="investment__item">
        <svg viewBox="0 0 24 24" fill="none" stroke="#091129" stroke-width="1.2"><rect x="2" y="6" width="17" height="13" rx="1.5"/><path d="M5 4h16v12"/><circle cx="8" cy="10" r="1.5"/><path d="M3 17l5-4 4 3 3-2 4 3"/></svg>
        <span>99 per listing for us to manage<br>images including editing, quality<br>control and delivery (10 Images)</span>
      </div>
      <span class="investment__divider"></span>
      <div class="investment__item">
        <svg viewBox="0 0 24 24" fill="none" stroke="#091129" stroke-width="1.2"><path d="M3 10l9-4 9 4-9 4z"/><path d="M3 10v8l9 4 9-4v-8"/><path d="M12 14v8"/><circle cx="12" cy="5" r="3"/><path d="M10.7 5l.9.9 1.6-1.7"/></svg>
        <span>Ask us about competitive<br>packages for photography<br>equipment if required</span>
      </div>
    </div>
  </div>

  <div class="abs photo" style="left:0;top:178px;width:220px;height:219px;background:linear-gradient(180deg,#6f8fb8 0%,#3d3a3c 45%,#6b6a55 75%,#5f7a3a 100%)" role="img" aria-label="Photograph of a dark weatherboard cottage with lit porch and gravel path at dusk"></div>
  <div class="abs photo" style="left:225px;top:178px;width:110px;height:108px;background:linear-gradient(180deg,#e8e6e2 0%,#cfc5b8 60%,#b7a891 100%)" role="img" aria-label="Photograph of a bright open-plan kitchen and dining area"></div>
  <div class="abs photo" style="left:341px;top:178px;width:99px;height:108px;background:linear-gradient(180deg,#6c7480 0%,#3a3f48 55%,#1c1e22 100%)" role="img" aria-label="Photograph of a black leather sofa in a grey living room"></div>
  <div class="abs photo" style="left:225px;top:291px;width:215px;height:106px;background:linear-gradient(180deg,#dcdcd8 0%,#9aa884 45%,#e9e6e1 100%)" role="img" aria-label="Photograph of a white bedroom with large windows to a green landscape"></div>
  <div class="abs photo" style="left:0;top:403px;width:104px;height:106px;background:linear-gradient(180deg,#e7e2da 0%,#d5cbbd 60%,#b59a72 100%)" role="img" aria-label="Photograph of a pale bathroom with timber vanity"></div>
  <div class="abs photo" style="left:110px;top:403px;width:110px;height:106px;background:linear-gradient(180deg,#8fa0c4 0%,#c4b6a0 50%,#6d5e4a 100%)" role="img" aria-label="Photograph of a stone and white farmhouse at twilight"></div>
  <div class="abs photo" style="left:225px;top:403px;width:215px;height:106px;background:linear-gradient(90deg,#4a3a2c 0%,#8a6f55 45%,#d9d7d2 100%)" role="img" aria-label="Photograph of a hallway decorated with framed artwork and rustic furniture"></div>

  <p class="abs summary">The KLD Real Estate Photography Editing and Support Service is the perfect solution for busy real estate professionals who want to take their business to the next level. Our service is affordable, flexible, and designed to help you showcase your listings in the best possible light.</p>
  <p class="abs cta">Contact us today to learn more about how we can help you</p>

  <p class="abs contact">
    <svg viewBox="0 0 24 24" fill="#d79a55"><path d="M6.6 10.8a15 15 0 006.6 6.6l2.2-2.2c.3-.3.7-.4 1-.2 1.1.4 2.3.6 3.6.6.6 0 1 .4 1 1V20c0 .6-.4 1-1 1A17 17 0 013 4c0-.6.4-1 1-1h3.5c.6 0 1 .4 1 1 0 1.3.2 2.5.6 3.6.1.3 0 .7-.2 1z"/></svg>
    +61 400 555 017<span class="contact__sep">|</span><span class="contact__web">www.<em>marcushale</em>.com.au</span>
  </p>

  <div class="abs avatar" style="left:346px;top:534px" role="img" aria-label="Portrait of Marcus Hale"></div>
  <p class="abs avatar-label" style="left:342px;top:578px">Marcus Hale</p>
</section>

</body>
</html>
```